Flyer-Design für Amerikanische Chiropraktik
Zielgruppe
Praxis für Amerikanische Chiropraktik
Zielgruppe: Gesundheitsbewusste Menschen, gerne gebildet, Affinität zu Sport/Yoga etc.
Flyer soll modern und hochwertig sein (Zielgruppe auch Privatversicherte und Büroleute)
Aufgabenstellung
Bitte keine Schnörkel.
Klare Linien. Straight einfach
Positive Vibes
Website ist nicht final fertig. Das blau/grau und das Grün wird aber aller Voraussicht nach Weiter verwendet. Falls das rot verwendet wird eher nicht so oft bitte.
Sehr gerne für die Überschriften die gleichen Balken unter den Überschriften für den Flyer verwenden.
Flyer bei Nordra Druck ist 99x210 mm (ich denke mit etwas Spiel am Rand für den Druck.) 6 Seiten.
Auf der letzten Seite (sollte die mittlere Rückseite sein) bitte Kontaktdaten und evtl Portraitbild.

```html
<!DOCTYPE html>
<html lang="de">
<head>
<meta charset="utf-8">
<title>Flyer Chiropraktik Kasimir Holt</title>
<link rel="stylesheet" href="https://fonts.googleapis.com/css2?family=Poppins:ital,wght@0,300;0,400;0,600;0,700;1,700&family=Open+Sans:ital,wght@0,400;0,600;1,400&display=swap">
<style>
:root{
  --gold:#b5a57b;
  --gold-dark:#a69466;
  --ink:#29292b;
  --paper:#ffffff;
  --stage:#ececec;
  --text:#2b2b2b;
}
*{box-sizing:border-box;margin:0;padding:0}
html,body{width:909px;height:1200px;overflow:hidden}
body{background:var(--stage);font-family:"Open Sans",Arial,sans-serif;color:var(--text);position:relative}
.spread{position:absolute;left:49px;width:810px;height:573px;display:flex;box-shadow:0 6px 18px rgba(0,0,0,.14)}
.spread--outside{top:18px}
.spread--inside{top:609px}
.panel{position:relative;width:270px;height:573px;overflow:hidden}
.panel--dark{background:var(--ink);color:#fff}
.panel--gold{background:var(--gold)}
.panel--white{background:var(--paper)}
.photo{position:absolute;left:0;right:0}
.brand{display:flex;align-items:center;gap:6px;font-family:"Poppins",sans-serif;font-weight:400;letter-spacing:.12em;text-transform:uppercase;font-size:9px;color:var(--ink)}
.brand__dot{flex:0 0 14px;width:14px;height:14px;border-radius:50%;border:1.5px solid currentColor}
.heading{font-family:"Poppins",sans-serif;font-weight:700;font-size:10.5px;line-height:1.25}
.heading em{font-style:normal;color:var(--gold)}
.rule{width:42px;height:2px;background:var(--gold);margin:4px 0 7px}
.copy{font-size:7.4px;line-height:1.42}
.copy p+p{margin-top:6px}
.copy .accent{color:var(--gold);font-weight:600}
.band{position:absolute;left:0;right:0;bottom:0;height:40px;background:var(--gold);display:flex;align-items:center;color:#fff;font-family:"Poppins",sans-serif;font-weight:700;font-style:italic;font-size:10.5px}
.band__line{height:2px;background:#fff;flex:0 0 40px}

/* cover */
.cover__brand{position:absolute;top:26px;left:0;right:0;justify-content:center}
.cover__photo{top:70px;height:252px;left:20px;right:20px;background:linear-gradient(160deg,#e9e1d4 0%,#cbb8a3 45%,#a68d78 100%)}
.cover__base{position:absolute;left:0;top:0;width:270px;height:573px}
.cover__title{position:absolute;left:0;right:0;top:392px;text-align:center;color:#fff;font-family:"Poppins",sans-serif}
.cover__title .light{font-weight:300;font-size:22px;line-height:1.1}
.cover__title .bold{font-weight:700;font-size:24px;line-height:1.15}
.cover__claim{margin-top:12px;color:var(--gold);font-weight:600;font-size:10px;letter-spacing:.03em}

/* contact */
.values{list-style:none;padding:26px 20px 0 20px}
.values li{display:flex;gap:8px;font-size:7.6px;line-height:1.4;margin-bottom:9px}
.values__icon{flex:0 0 13px;height:13px;border-radius:50%;border:1.2px solid var(--gold);margin-top:1px}
.contact__rule{height:2px;background:var(--gold);margin:14px 20px 14px}
.contact{text-align:center;font-size:8px;line-height:1.55;font-style:normal}
.contact__name{color:var(--gold);font-family:"Poppins",sans-serif;font-weight:700;font-size:9.5px}
.contact__address{margin-top:6px}
.contact__web{color:var(--gold);font-weight:600;margin-top:4px}
.contact__rule--short{margin:12px 20px 0}
.contact__greeting{position:absolute;left:0;width:140px;top:395px;text-align:center;color:var(--gold);font-family:"Poppins",sans-serif;font-weight:700;font-size:12px;line-height:1.25}
.contact__brand{position:absolute;left:16px;width:122px;top:480px;color:#fff;line-height:1.35}
.contact__brand-name{display:flex;flex-direction:column}
.contact__portrait{right:0;left:auto;width:128px;bottom:0;height:150px;background:linear-gradient(180deg,#3a3936 0%,#8a7d6e 55%,#cfd3d8 100%)}

/* indications flap */
.flap__photo{top:0;height:96px;background:linear-gradient(135deg,#f1efea 0%,#cfcac0 50%,#6b5a48 100%);clip-path:polygon(0 0,100% 0,100% 78%,50% 100%,0 78%)}
.flap__body{position:absolute;top:104px;left:20px;right:18px}
.flap__list{list-style:none;margin-top:6px;font-size:7.6px;line-height:1.65}
.flap__list li::before{content:"";display:inline-block;width:4px;height:4px;border-radius:50%;background:var(--gold);margin-right:6px;vertical-align:middle}
.flap__gold{position:absolute;left:0;right:0;bottom:0;height:178px;background:var(--gold);color:var(--ink);padding:20px 20px 0}
.flap__gold .rule{background:var(--ink)}

/* inside */
.inside__body{position:absolute;top:20px;left:20px;right:18px}
.block+.block{margin-top:12px}
.block--spaced{margin-top:18px}
.causes__photo{top:0;height:112px;background:linear-gradient(150deg,#eeece8 0%,#d9d3ca 50%,#b9ab97 100%);clip-path:polygon(0 0,100% 0,100% 86%,50% 100%,0 86%)}
.causes__body{position:absolute;top:124px;left:20px;right:18px}
.causes__body .heading{color:#fff}
.causes__sub{margin-top:12px}
.cause{display:flex;gap:10px;margin-top:12px}
.cause__icon{flex:0 0 26px;height:26px;border-radius:50%;border:1.5px solid #fff}
.cause__title{font-family:"Poppins",sans-serif;font-weight:600;font-size:9px;color:var(--gold)}
.cause__text{font-size:7.6px;line-height:1.4}
.band--web{justify-content:center;font-style:normal}
.band__quote--left{margin-left:12px}
.band__quote--right{margin-left:14px;margin-right:12px}
.uses{list-style:none;margin-top:8px;font-size:7.6px;line-height:1.4;color:var(--gold-dark);font-weight:600;font-style:italic}
.uses li{display:flex;gap:6px;margin-bottom:3px}
.uses li::before{content:"";flex:0 0 4px;height:4px;margin-top:4px;border-radius:50%;background:var(--gold)}
</style>
</head>
<body>

<!-- Außenseite -->
<section class="spread spread--outside">

  <article class="panel panel--dark flap">
    <div class="photo flap__photo" role="img" aria-label="Foto eines Chiropraktik-Instruments auf der Behandlungsliege"></div>
    <div class="flap__body">
      <h2 class="heading">Gerne besuchen uns Menschen mit:</h2>
      <div class="rule"></div>
      <ul class="flap__list">
        <li>Rückenschmerzen</li>
        <li>Chronischer Stress</li>
        <li>Kopfschmerzen und Migräne</li>
        <li>Nackenverspannungen</li>
        <li>Schulter- und Armschmerzen</li>
        <li>Karpaltunnelsyndrom</li>
        <li>Ischiassyndrom</li>
        <li>Schwindel und Tinnitus</li>
        <li>Haltungsproblemen</li>
        <li>Taubheit in Händen oder Füßen</li>
      </ul>
    </div>
    <div class="flap__gold">
      <h2 class="heading">Blockierte Gelenke</h2>
      <div class="rule"></div>
      <p class="copy">Sanfte, gezielte Impulse lösen punktuelle Dehnungen der Gelenke und nehmen den Druck. Sie senden Reize aus, die im Gehirn die Steuerung der Gelenke und Muskeln verbessern.</p>
    </div>
  </article>

  <article class="panel panel--dark contact-panel">
    <ul class="values">
      <li><span class="values__icon"></span><span>Wir sind Experten auf unserem Gebiet.</span></li>
      <li><span class="values__icon"></span><span>Arbeiten nach neuesten wissenschaftlichen Kenntnissen. Sanfte und zielgerichtete Behandlung.</span></li>
      <li><span class="values__icon"></span><span>Profitieren Sie von langjähriger praktischer Erfahrung und modernen neurowissenschaftlichen Aspekten in der chiropraktischen Behandlung.</span></li>
      <li><span class="values__icon"></span><span>Wir sind mit Freude und Engagement für Dich und Deine Gesundheit da.</span></li>
    </ul>
    <div class="contact__rule"></div>
    <address class="contact">
      <div class="contact__name">Kasimir Holt</div>
      <div>Heil- und Chiropraktiker,<br>B.Sc. Physiotherapie</div>
      <div class="contact__address">Lindenweg 12 | 83700 Talheim</div>
      <div>Tel: 0151/48295617</div>
      <div>praxis@chiropraktik-holt.de</div>
      <div class="contact__web">www.chiropraktik-holt.de</div>
    </address>
    <div class="contact__rule contact__rule--short"></div>
    <p class="contact__greeting">Wir freuen uns<br>auf Dich!</p>
    <div class="brand contact__brand"><span class="brand__dot"></span><span class="contact__brand-name"><span>Chiropraktik</span><span>Kasimir Holt</span></span></div>
    <div class="photo contact__portrait" role="img" aria-label="Porträtfoto des Chiropraktikers, sitzend im weißen Shirt"></div>
  </article>

  <article class="panel panel--gold cover">
    <svg class="cover__base" viewBox="0 0 270 573" aria-hidden="true">
      <polygon points="0,318 135,348 270,318 270,573 0,573" fill="#29292b"/>
    </svg>
    <div class="brand cover__brand"><span class="brand__dot"></span>Chiropraktik Kasimir Holt</div>
    <div class="photo cover__photo" role="img" aria-label="Foto: Chiropraktiker umarmt eine Patientin"></div>
    <div class="cover__title">
      <div class="light">Ihr weg zu mehr</div>
      <div class="bold">Wohlbefinden</div>
      <div class="cover__claim">MODERN.URSÄCHLICH.ANDERS.</div>
    </div>
  </article>
</section>

<!-- Innenseite -->
<section class="spread spread--inside">

  <article class="panel panel--white">
    <div class="inside__body">
      <div class="block">
        <h2 class="heading">Was ist <em>Amerikanische Chiropraktik?</em></h2>
        <div class="rule"></div>
        <div class="copy">
          <p>Amerikanische Chiropraktik ist eine eigenständige, ganzheitliche und vitalistische Form der Gesundheitspflege, die darauf ausgerichtet ist, Gesundheit und Funktion des menschlichen Körpers wiederherzustellen und zu erhalten.</p>
          <p>Sie ist sowohl eine evidenzbasierte Wissenschaft als auch eine Heilkunst und eine Philosophie, die nach der optimalen Funktion des Nervensystems strebt.</p>
        </div>
      </div>
      <div class="block">
        <h2 class="heading">Wie funktioniert <em>Chiropraktik?</em></h2>
        <div class="rule"></div>
        <div class="copy">
          <p>Der Körper wird von seinem Nervensystem gesteuert. Es ist dafür verantwortlich, wie ein Mensch seine Umwelt wahrnimmt und durch das Leben geht. Über das Nervensystem empfängt und sendet das Gehirn fortwährend Informationen an Organe, Muskeln und alle anderen Strukturen. Seine optimale Funktion ist demnach von größter Bedeutung.</p>
          <p>Im besten Fall werden Körper und Psyche über das Nervensystem in Balance gehalten. Dazu muss alles störungsfrei miteinander vernetzt sein. Fehlstellungen und Blockaden können die Vernetzung stören: Es kommt zu sogenannten Subluxationen. Das physische und psychische Gleichgewicht gerät ins Wanken. Die Folgen können sehr vielfältig sein. Muskelverspannungen, Nackenschmerzen, Kopfschmerzen oder Rückenschmerzen können die Folge sein. Oft bleiben solche <span class="accent">Subluxationen</span> über Jahre unbemerkt, bevor sie Schmerzen und/oder psycho-emotionale Symptome verursachen.</p>
        </div>
      </div>
    </div>
    <div class="band"><span class="band__line"></span><span class="band__quote--left">"Time to Connect Your Brain."</span></div>
  </article>

  <article class="panel panel--dark">
    <div class="photo causes__photo" role="img" aria-label="Foto einer chiropraktischen Behandlung am Rücken"></div>
    <div class="causes__body">
      <h2 class="heading">Was ist eigentlich eine <em>Subluxation?</em></h2>
      <div class="rule"></div>
      <p class="copy">Wir definieren eine vertebrale Subluxation als ein dysfunktionales Gebiet in der Wirbelsäule, dass sich aufgrund seines Einflusses auf das Nervensystem negativ auf die Gesundheit und das Wohlbefinden auswirkt. Die Funktion der Wirbelsäule als wichtiger Informationsgeber für das Gehirn ist gestört.</p>
      <h2 class="heading causes__sub">Ursachen für eine <em>Subluxation</em></h2>
      <div class="cause"><span class="cause__icon"></span><div><div class="cause__title">Physischer Stress</div><div class="cause__text">wie z.B. Trauma (Brüche etc.) Unfälle, langes Sitzen, Bewegungsmangel</div></div></div>
      <div class="cause"><span class="cause__icon"></span><div><div class="cause__title">Toxischer Stress</div><div class="cause__text">wie z.B. Zigaretten, Alkohol, Drogen, Abgase, Medikamente, Übersäuerung</div></div></div>
      <div class="cause"><span class="cause__icon"></span><div><div class="cause__title">Psychischer Stress</div><div class="cause__text">Macht einen großen Anteil aus. Druck und hohe Anforderungen im Beruf, Alltagsstress, Schlafmangel, Sorgen, Überforderung.</div></div></div>
    </div>
    <div class="band band--web">www.chiropraktik-holt.de</div>
  </article>

  <article class="panel panel--white">
    <div class="inside__body">
      <div class="block">
        <h2 class="heading">Wie helfen wir? <em>Die Justierung</em></h2>
        <div class="rule"></div>
        <p class="copy">Die chiropraktische Justierung korrigiert eine Subluxation, indem sie das schadhafte neurologische Muster durchbricht. Durch einen sanften und gezielten Impuls wird die physiologische Beweglichkeit und Position eines Gelenkes wieder hergestellt und faszialer Adhäsionen gelöst. Die Impulse führen zu einer messbaren Verbesserung in der Funktion hinsichtlich der Beziehung zwischen Nervensystem und Bewegungsapparat (Lindqvist et al., 2021). Der chiropraktische Impuls wirkt auf struktureller Ebene (am Gelenk) und im Nervensystem. Der Informationsfluss zwischen Körper und Nervensystem wird harmonisiert und Selbstheilungskräfte aktiviert, um dir eine volle Funktionalität und mehr Lebensqualität zu ermöglichen.</p>
      </div>
      <div class="block block--spaced">
        <h2 class="heading">Für wen?</h2>
        <div class="rule"></div>
        <p class="copy">Die Amerikanische Chiropraktik verfolgt einen ganzheitlichen und ursachenbezogenen Ansatz, wodurch sich vielseitige Anwendungsbereiche ergeben. Unser Angebot reicht von Gesundheitsvorsorge bis hin zur Behandlung von bereits existierenden Störungen und Symptomen. Anwendungsgebiete</p>
        <ul class="uses">
          <li>Chiropraktik zur Leistungssteigerung im Sport</li>
          <li>Chiropraktik als konstante Begleitung für mehr Balance und Wohlbefinden im Alltag</li>
          <li>Chiropraktik in der Schwangerschaft</li>
          <li>Chiropraktik als effektive Methode für die Behandlung von Schmerzen und Einschränkungen des Bewegungsapparats und des Nervensystems</li>
        </ul>
      </div>
    </div>
    <div class="band"><span class="band__quote--right">"Time to Connect Your Brain."</span><span class="band__line"></span></div>
  </article>
</section>

</body>
</html>
```